KVRo Business Cards

We need a business card design. We are a Technology (Audio Visual) design, sales and installation company. Looking for a double sided design, clean

Contact Information for Business Card

Clean, modern look, 2 sided

Font styles to use
Sans Serif

```html
<!DOCTYPE html>
<html lang="en">
<head>
<meta charset="utf-8">
<title>KVRo Business Cards</title>
<link rel="stylesheet" href="https://fonts.googleapis.com/css2?family=Fira+Sans:wght@400;500;600;800&display=swap">
<style>
  :root {
    --orange: #fe8307;
    --ink: #0d1112;
    --white: #ffffff;
    --page: #ffffff;
  }
  * { box-sizing: border-box; margin: 0; padding: 0; }
  html, body {
    width: 966px; height: 1200px; overflow: hidden;
    background: var(--page);
    font-family: "Fira Sans", sans-serif;
  }
  .sheet { position: relative; width: 966px; height: 1200px; }

  .card-front {
    position: absolute; left: 112px; top: 100px;
    width: 746px; height: 426px;
    background: var(--orange);
    display: flex; align-items: center; justify-content: center;
  }
  .brand-name {
    color: var(--white);
    font-weight: 800;
    font-size: 108px;
    letter-spacing: -2px;
    line-height: 1;
    margin-top: -18px;
  }

  .card-back {
    position: absolute; left: 112px; top: 660px;
    width: 746px; height: 428px;
    border: 3px solid var(--ink);
    background: var(--white);
    overflow: hidden;
  }
  .identity-block {
    position: absolute; left: 0; top: 0;
    width: 347px; height: 154px;
    background: var(--ink);
    color: var(--white);
  }
  .person-icon { position: absolute; left: 20px; top: 27px; width: 24px; height: 26px; }
  .person-name {
    position: absolute; left: 59px; top: 22px;
    font-size: 26px; font-weight: 600; letter-spacing: 0.3px;
  }
  .person-role {
    position: absolute; left: 71px; top: 58px;
    font-size: 18px; font-weight: 400;
  }

  .contact-block {
    position: absolute; left: 347px; top: 154px;
    right: 0; bottom: 0;
    background: var(--orange);
    color: var(--white);
  }
  .contact-list { list-style: none; position: absolute; left: 35px; top: 30px; }
  .contact-item {
    position: relative; height: 36px;
    display: flex; align-items: center;
    font-size: 21px; letter-spacing: 0.4px;
  }
  .contact-icon { width: 26px; height: 26px; flex: none; }
  .contact-sep { width: 34px; text-align: right; padding-right: 10px; flex: none; }
  .contact-value { margin-left: 2px; }
  .contact-item.continued { padding-left: 62px; margin-top: -3px; }
  .contact-icon * { fill: none; stroke: var(--white); stroke-width: 1.8; stroke-linecap: round; stroke-linejoin: round; }
</style>
</head>
<body>
<main class="sheet">
  <section class="card-front" aria-label="Card front">
    <span class="brand-name">KVRo</span>
  </section>

  <section class="card-back" aria-label="Card back">
    <div class="identity-block">
      <svg class="person-icon" viewBox="0 0 24 26" aria-hidden="true">
        <circle cx="14" cy="9" r="6.5" fill="none" stroke="#fff" stroke-width="2"/>
        <path d="M9.5 14 L3 24" stroke="#fff" stroke-width="2" stroke-linecap="round"/>
      </svg>
      <span class="person-name">Arun Velmoran</span>
      <span class="person-role">chief executive officer</span>
    </div>

    <div class="contact-block">
      <ul class="contact-list">
        <li class="contact-item">
          <svg class="contact-icon" viewBox="0 0 26 26" aria-hidden="true"><rect x="6" y="1.5" width="14" height="23" rx="1.5"/><path d="M11 21h4"/></svg>
          <span class="contact-sep">:</span><span class="contact-value">(000)000-123</span>
        </li>
        <li class="contact-item">
          <svg class="contact-icon" viewBox="0 0 26 26" aria-hidden="true"><rect x="2" y="6" width="22" height="14"/><path d="M2 6l11 8 11-8"/></svg>
          <span class="contact-sep">:</span><span class="contact-value">email@your.com</span>
        </li>
        <li class="contact-item">
          <svg class="contact-icon" viewBox="0 0 26 26" aria-hidden="true"><circle cx="13" cy="13" r="10"/><ellipse cx="13" cy="13" rx="4.5" ry="10"/><path d="M3 13h20M5 7.5h16M5 18.5h16"/></svg>
          <span class="contact-sep">:</span><span class="contact-value">www.yourcompany.com</span>
        </li>
        <li class="contact-item">
          <svg class="contact-icon" viewBox="0 0 26 26" aria-hidden="true"><path d="M2 13L13 3l11 10M6 10v12M20 10v12"/></svg>
          <span class="contact-sep">:</span><span class="contact-value">Address line 1</span>
        </li>
        <li class="contact-item">
          <svg class="contact-icon" viewBox="0 0 26 26" aria-hidden="true"><path d="M6 20.5A9 9 0 1 1 13 23"/><circle cx="13" cy="11" r="3.5"/></svg>
          <span class="contact-sep">:</span><span class="contact-value">Address line 2</span>
        </li>
        <li class="contact-item continued">
          <span class="contact-value">Address line 3</span>
        </li>
      </ul>
    </div>
  </section>
</main>
</body>
</html>
```